Swimming pool service business postcard redesign

We need a fresh post card design for our pool service business based in San Diego called Tide Sweepers. We are a family based, local residential pool cleaning and maintenance company. we need an offer to stand out, our logo, our colors, etc on a 5.5x8 inch full color post card.

```html
<!DOCTYPE html>
<html lang="en">
<head>
<meta charset="utf-8">
<title>Tide Sweepers – Service Terms Postcard</title>
<link href="https://fonts.googleapis.com/css2?family=Tinos:ital,wght@0,400;0,700;1,400&display=swap" rel="stylesheet">
<style>
  :root{
    --page-bg:#e4e4e4;
    --card-white:#ffffff;
    --ink:#1d1d1d;
    --ocean-light:#6fb0de;
    --ocean-mid:#3b86c4;
    --ocean-deep:#1c5f9c;
    --coral:#e2603f;
    --coral-deep:#c9482a;
    --on-dark:#ffffff;
    --brand-blue:#2d6fb0;
    --sun:#ffd76a;
  }
  *{box-sizing:border-box;margin:0;padding:0}
  html,body{width:988px;height:1200px;overflow:hidden}
  body{background:var(--page-bg);font-family:"Tinos","Times New Roman",serif;color:var(--ink);position:relative}

  .card{position:absolute;left:121px;width:746px;height:511px;background:var(--card-white);overflow:hidden}
  .card--front{top:56px}
  .card--back{top:612px;height:513px}

  /* front: left column */
  .intro{position:absolute;left:0;top:0;width:283px;height:100%;
    background:linear-gradient(180deg,#ffffff 0%,#ffffff 45%,#eef3f6 65%,#e9eef2 82%,#ffffff 100%)}
  .brand{position:absolute;left:42px;top:92px;display:flex;align-items:center;gap:10px}
  .brand__dot{width:26px;height:26px;border-radius:50%;background:var(--brand-blue)}
  .brand__name{font-weight:700;font-size:27px;color:var(--brand-blue);letter-spacing:.5px}
  .charges{position:absolute;left:32px;top:234px;width:222px}
  .charges h2{font-size:13.5px;font-weight:700;margin-bottom:15px;letter-spacing:.2px}
  .charges ol{list-style:none}
  .charges li{display:flex;font-size:11px;line-height:12.4px}
  .charges li span{width:21px;flex:none}
  .charges p{font-size:11px;line-height:14.6px;margin-top:12px}

  /* front: right photo panel */
  .terms{position:absolute;left:283px;top:0;right:0;height:100%;
    background:linear-gradient(160deg,var(--ocean-light) 0%,var(--ocean-mid) 45%,var(--ocean-deep) 100%);
    color:var(--on-dark)}
  .terms__photo{position:absolute;inset:0;background:linear-gradient(180deg,rgba(255,255,255,0) 40%,rgba(120,190,230,.25) 70%,rgba(20,70,120,.3) 100%)}
  .terms__body{position:absolute;left:41px;top:32px;width:376px}

  .clause h3{font-size:13.5px;font-weight:400;letter-spacing:.3px;display:flex;line-height:14px}
  .clause h3 b{font-weight:400;width:21px;flex:none}
  .clause p,.clause li{font-size:10.7px;line-height:12.2px}
  .clause{margin-bottom:10px}
  .clause ul{list-style:none}
  .clause li{display:flex}
  .clause li i{font-style:normal;width:21px;flex:none}
  .clause .indent{padding-left:21px}
  .clause em{font-style:italic}
  .tier{font-weight:700;padding-left:21px}
  .tier span{display:inline-block;width:26px}

  /* back */
  .details{position:absolute;left:0;top:0;width:414px;height:415px;background:var(--coral);color:var(--on-dark);padding:34px 0 0 34px}
  .details .clause{width:352px;margin-bottom:13px}
  .details .clause h3{margin-bottom:1px}
  .schedule{position:absolute;left:32px;top:424px;width:360px;font-size:10.7px;line-height:12.3px}

  /* back: offer */
  .offer{position:absolute;left:414px;top:0;right:0;height:100%;
    background:linear-gradient(165deg,var(--ocean-light) 0%,var(--ocean-mid) 50%,var(--ocean-deep) 100%);
    color:var(--on-dark);text-align:center;padding:46px 30px 0}
  .offer__kicker{font-size:13.5px;letter-spacing:2.5px}
  .offer__rule{width:60px;height:2px;background:var(--sun);margin:12px auto 16px}
  .offer__amount{font-weight:700;font-size:84px;line-height:1;color:var(--sun)}
  .offer__off{font-weight:700;font-size:30px;letter-spacing:4px;margin-top:2px}
  .offer__what{font-size:15px;line-height:19px;margin-top:12px}
  .offer__badge{display:inline-block;margin-top:20px;background:var(--coral);border-radius:4px;padding:9px 18px;font-weight:700;font-size:14px;letter-spacing:1px}
  .offer__list{list-style:none;text-align:left;margin:26px auto 0;width:220px}
  .offer__list li{display:flex;align-items:center;gap:9px;font-size:12.5px;line-height:22px}
  .offer__list svg{flex:none}
  .offer__fine{position:absolute;left:24px;right:24px;bottom:22px;font-size:9.5px;line-height:11.5px;opacity:.85}
</style>
</head>
<body>

<section class="card card--front">
  <div class="intro">
    <div class="brand">
      <div class="brand__dot"></div>
      <div class="brand__name">Tide Sweepers</div>
    </div>
    <div class="charges">
      <h2>SERVICE CHARGES</h2>
      <ol>
        <li><span>a)</span>All new Customers are required to have an initial deep filter cleaning and complete equipment inspection.</li>
        <li><span>b)</span>Additional filter cleanings will be performed on a scheduled basis, or as needed, at an additional charge.</li>
        <li><span>c)</span>Replacement cartridges, grids, and other filter parts will be replaced as needed at an additional charge.</li>
        <li><span>d)</span>Any request deemed as service calls, repairs, and evaluations are at an additional charge.</li>
      </ol>
      <p>TIDE SWEEPERS performs filter cleanings to maintain optimal equipment function. These cleanings are charged at time of completion.</p>
    </div>
  </div>

  <div class="terms" role="img" aria-label="Photo of a sunlit backyard swimming pool with wooden deck, tinted blue">
    <div class="terms__photo"></div>
    <div class="terms__body">
      <div class="clause">
        <h3><b>1</b>LIABILITY</h3>
        <p class="indent">TIDE SWEEPERS is not liable for pre-existing conditions or equipment failures including but not limited to pumps, motors, filters, or pool structures.</p>
      </div>
      <div class="clause">
        <h3><b>2.</b>CLIENT RESPONSIBILITIES</h3>
        <ul>
          <li><i>•</i><span><em>Water Level:</em> Clients must maintain proper pool/spa/fountain water levels. In most cases, the skimmer opening should be submerged halfway underwater. Proper water level ensures effective filtration and chemical balance.</span></li>
          <li style="margin-top:11px"><i>•</i><em>Access &amp; Pool Preparation:</em></li>
          <li><i>o</i>Clear, safe access to the pool area must be provided on the day of service.</li>
          <li><i>o</i>Pool toys, floating mats, and solar covers must be removed prior to service.</li>
          <li><i>o</i>Safety features, including nets or covers, must be removed before our visit. The Company will not remove or reinstall these items.</li>
          <li><i>o</i>Failure to prepare the pool area may result in incomplete service, and no reschedule or credit is guaranteed for such missed services.</li>
        </ul>
      </div>
      <div class="clause">
        <h3><b>3.</b>SERVICES PROVIDED</h3>
        <p>The Company offers the following service tiers:</p>
        <p class="tier"><span>a)</span>Basic Service</p>
        <ul>
          <li><i>•</i>Two visits per month.</li>
          <li><i>•</i>Diagnostic testing and adjustment for chlorine, pH, and complete water balance.</li>
        </ul>
        <p class="tier" style="font-weight:400"><span>b)</span>Basic Plus Service</p>
        <ul><li><i>•</i>Includes Basic Service, plus quarterly filter cleaning and an equipment evaluation.</li></ul>
        <p class="tier"><span>c)</span>Full Service</p>
        <ul>
          <li><i>•</i>No less than four visits per month.</li>
          <li><i>•</i>Chemical testing and balance, floating chlorinator maintenance, debris removal, wall and tile brushing, basket emptying, and filter cleaning (for filters under 200 sq. ft).</li>
        </ul>
        <p class="tier"><span>d)</span>Extra Full Service</p>
        <ul>
          <li><i>•</i>Recommended for pools prone to heavy debris.</li>
          <li><i>•</i>Includes all Full Service offerings, with six visits per month for weekly cleanings and chemical treatments.</li>
        </ul>
      </div>
    </div>
  </div>
</section>

<section class="card card--back">
  <div class="details">
    <div class="clause"><h3><b>4.</b>CHEMICALS AND MAINTENANCE</h3></div>
    <div class="clause">
      <h3><b>5.</b>REPAIRS AND EQUIPMENT MAINTENANCE</h3>
      <ul>
        <li><i>•</i>All repair requests will be evaluated, quoted, and approved by the Client before execution.</li>
        <li><i>•</i>Repairs related to county-mandated safety updates will be billed separately.</li>
      </ul>
    </div>
    <div class="clause">
      <h3><b>6.</b>WATER CLARITY AND QUALITY GUARANTEE</h3>
      <ul>
        <li><i>•</i>The Company ensures proper chemical balance to prevent algae and bacteria growth.</li>
        <li><i>•</i>Water clarity depends on three factors: chemical balance, filtration, and circulation. The Company guarantees water clarity only as it pertains to chemistry.</li>
      </ul>
    </div>
    <div class="clause">
      <h3><b>7.</b>EXCLUSIONS</h3>
      <ul>
        <li><i>•</i>Services do not include repairing or addressing structural damage, underground leaks, or equipment not maintained per industry standards.</li>
        <li><i>•</i>Missed visits due to inaccessible areas (e.g., locked gates or unremoved covers) will not be refunded or rescheduled.</li>
      </ul>
    </div>
    <div class="clause">
      <h3><b>8.</b>ADDITIONAL INFORMATION</h3>
      <ul>
        <li><i>•</i>Safety: Swimming is safe 30 minutes after chemical treatment.</li>
        <li><i>•</i>On-Site Records: Service records will be kept in the pool's timer box and service tags left at the property.</li>
        <li><i>•</i>Initial Start-Up Fee: $85 applies to all new service agreements.</li>
        <li><i>•</i>Service Changes: Service terms and rates are subject to change with 30 days' notice.</li>
      </ul>
    </div>
  </div>
  <p class="schedule">The service plan includes either 48 or 24 scheduled visits based on a 52-week year, with service pauses during the week of Thanksgiving, Easter, Christmas, and a fourth week at our discretion, with prior notification. Prior to any pause in service, we will take measures to maintain water quality before each scheduled break."</p>

  <aside class="offer">
    <p class="offer__kicker">NEW CUSTOMER OFFER</p>
    <div class="offer__rule"></div>
    <p class="offer__amount">$50</p>
    <p class="offer__off">OFF</p>
    <p class="offer__what">your first month of<br>Full Service pool care</p>
    <p class="offer__badge">START-UP FEE WAIVED</p>
    <ul class="offer__list">
      <li><svg width="14" height="14" viewBox="0 0 14 14"><path d="M2 7.5l3 3 7-7" fill="none" stroke="#ffd76a" stroke-width="2.2"/></svg>Family-owned &amp; local</li>
      <li><svg width="14" height="14" viewBox="0 0 14 14"><path d="M2 7.5l3 3 7-7" fill="none" stroke="#ffd76a" stroke-width="2.2"/></svg>Serving San Diego homes</li>
      <li><svg width="14" height="14" viewBox="0 0 14 14"><path d="M2 7.5l3 3 7-7" fill="none" stroke="#ffd76a" stroke-width="2.2"/></svg>Clear water, guaranteed</li>
    </ul>
    <p class="offer__fine">Mention this card when booking. Valid for new residential service agreements only.</p>
  </aside>
</section>

</body>
</html>
```